Web Design Project - vR Advise

We want to modernise our web page profile. We have an existing web site that we are particularly not proud of (www.vradvise.com.au).
We have started to build a new web site using Joomla and we like the structure of it, but we need it to be professionally designed and implemented.

This current development site can be viewed here: dev.vradvise.com.au

We would like a complete design for the entire website, ready for deployment.

(We still need to finalise the content, as we have just developed new products that we hope to launch in August both on this web site and by a Vendor Forum.)
Updates

Target Market(s)

Larger companies where the robustness of their IT infrastructure is critical. Our tools and services provide for monitoring of every device

Industry/Entity Type

Build

Requirements
Must have
• Responsive design for different screen sizes.

BrightDock help desk software integrated with the website.
Currently can be viewed at support.vradvise.com.au
Brightdock only supports custom css.

Nice to have
• Customer experience testimonials in a rotating banner
Chirpr and Pagebook links in the footer
We use Avenir as a company font.
Use company colours as in the logo (green and blue)

```html
<!DOCTYPE html>
<html lang="en">
<head>
<meta charset="utf-8">
<title>vR Advise</title>
<link rel="stylesheet" href="https://fonts.googleapis.com/css2?family=Open+Sans:wght@300;400;600;700&display=swap">
<style>
:root{
  --green:#33c86c;
  --green-dark:#27b25c;
  --blue:#3a8fdb;
  --blue-dark:#2f7fc9;
  --grey-bg:#eeeeee;
  --ink:#111111;
  --text:#444444;
  --client:#3a3a3a;
  --orange:#f39a2b;
  --charcoal:#2d2d2d;
  --footer:#141414;
  --white:#ffffff;
}
*{box-sizing:border-box;margin:0;padding:0}
html,body{width:1200px;height:2603px;overflow:hidden}
body{font-family:"Open Sans",Arial,sans-serif;color:var(--text);background:var(--white);position:relative}
section,header,footer{position:absolute;left:0;width:1200px}

/* Header */
.site-header{top:0;height:208px;background:var(--white)}
.brand{position:absolute;left:91px;top:66px;display:flex;align-items:center;gap:14px}
.brand-mark{width:56px;height:56px;border-radius:50%;background:var(--green)}
.brand-name{font-size:36px;font-weight:700;color:var(--blue-dark)}
.main-nav{position:absolute;left:338px;top:57px;height:65px;display:flex;background:var(--blue);box-shadow:0 3px 6px rgba(0,0,0,.12)}
.main-nav a{display:flex;align-items:center;justify-content:center;color:var(--white);text-decoration:none;font-size:20px;border-right:1px solid rgba(255,255,255,.18);height:65px}
.main-nav a:last-child{border-right:0}
.main-nav a.active{border-top:6px solid var(--green);padding-bottom:6px}

/* Hero */
.hero{top:208px;height:474px;background:radial-gradient(ellipse at 50% 40%,#45d57c 0%,var(--green) 55%,var(--green-dark) 100%);text-align:center;color:var(--white)}
.hero h1{position:absolute;top:170px;width:100%;font-size:56px;font-weight:700;letter-spacing:.5px}
.hero p{position:absolute;top:262px;width:100%;font-size:28px;font-weight:300}

/* Offerings */
.offerings{top:682px;height:580px;background:var(--grey-bg)}
.offer{position:absolute;top:70px;width:330px;text-align:center}
.offer h2{font-size:46px;font-weight:700;color:var(--ink);line-height:1.2}
.offer-icons{display:flex;justify-content:center;gap:18px;margin-top:26px}
.offer-item{width:92px;display:flex;flex-direction:column;align-items:center}
.icon-circle{width:78px;height:78px;border-radius:50%;display:flex;align-items:center;justify-content:center}
.icon-circle.blue{background:var(--blue)}
.icon-circle.orange{background:var(--orange)}
.icon-circle.dark{background:var(--charcoal)}
.offer-item span{margin-top:8px;font-size:16px;font-weight:300;line-height:1.3;color:#555}
.offer p{margin:24px auto 0;width:300px;font-size:13.5px;line-height:1.45;text-align:justify;color:#333}
.btn{display:block;margin:0 auto;color:var(--white);font-size:12px;font-weight:700;height:34px;line-height:34px;border-radius:2px;text-decoration:none}
.btn-blue{background:var(--blue);width:104px;margin-top:26px}
.btn-green{background:var(--green);display:table;padding:0 16px;margin-top:24px}

/* Testimonials */
.testimonials{top:1262px;height:479px;background:var(--blue);color:var(--white)}
.testimonials h2{position:absolute;left:78px;top:80px;font-size:46px;font-weight:700}
.portrait{position:absolute;left:89px;top:162px;width:228px;height:228px;border-radius:50%;border:4px solid var(--white);background:linear-gradient(160deg,#f0ede9 0%,#e3b7a3 45%,#c8312f 100%)}
.quote{position:absolute;left:396px;top:192px;width:710px;font-size:17px;line-height:1.5;text-align:justify}
.quote cite{display:block;margin-top:14px;font-style:normal;font-size:13px}
.arrows{position:absolute;display:flex;gap:18px}
.testimonials .arrows{left:1116px;top:438px}
.clients .arrows{left:1116px;top:398px}

/* Clients */
.clients{top:1741px;height:438px;background:var(--white)}
.clients h2{position:absolute;left:86px;top:82px;font-size:46px;font-weight:700;color:var(--ink)}
.client-row{position:absolute;left:90px;top:190px;width:1020px;height:150px;display:flex;align-items:center;justify-content:space-between}
.client{white-space:nowrap;font-weight:600;font-size:23px;color:var(--client)}

/* Footer */
.site-footer{top:2179px;height:424px;background:var(--footer);color:var(--white)}
.site-footer h2{position:absolute;left:86px;top:80px;font-size:46px;font-weight:700}
.social{position:absolute;left:86px;top:176px;display:flex;gap:34px}
.social a{display:flex;flex-direction:column;align-items:center;gap:8px;color:var(--white);text-decoration:none;font-size:13px;width:78px}
.social .dot{width:78px;height:78px;border-radius:50%;background:var(--blue)}
.copyright{position:absolute;left:86px;top:320px;font-size:13px}
</style>
</head>
<body>

<header class="site-header">
  <div class="brand"><span class="brand-mark"></span><span class="brand-name">vR Advise</span></div>
  <nav class="main-nav">
    <a class="active" href="#" style="width:112px">Home</a>
    <a href="#" style="width:133px">Services</a>
    <a href="#" style="width:130px">Support</a>
    <a href="#" style="width:135px">Products</a>
    <a href="#" style="width:136px">About Us</a>
    <a href="#" style="width:125px">Contact</a>
  </nav>
</header>

<section class="hero" role="img" aria-label="Green banner with a soft network of connected nodes">
  <h1>Any device, any platform, anywhere</h1>
  <p>Cross-domain, performance and service level monitoring and management</p>
</section>

<section class="offerings">
  <div class="offer" style="left:72px">
    <h2>Services</h2>
    <div class="offer-icons">
      <div class="offer-item"><div class="icon-circle blue"><svg width="42" height="38" viewBox="0 0 42 38"><rect x="3" y="3" width="36" height="24" rx="2" fill="none" stroke="#fff" stroke-width="3"/><rect x="17" y="27" width="8" height="6" fill="#fff"/><rect x="11" y="32" width="20" height="3" fill="#fff"/></svg></div><span>Consulting Services</span></div>
      <div class="offer-item"><div class="icon-circle orange"></div><span>Professional Services</span></div>
      <div class="offer-item"><div class="icon-circle dark"></div><span>Productised Services</span></div>
    </div>
    <p>Our extensive Professional Service experience and expertise fuels the architecture and delivery practices, ensuring that what we propose to our customers we also deploy, manage and support.</p>
    <a class="btn btn-blue" href="#">Learn More</a>
    <a class="btn btn-green" href="#">Specialised Services</a>
  </div>

  <div class="offer" style="left:435px">
    <h2>Products</h2>
    <div class="offer-icons">
      <div class="offer-item"><div class="icon-circle blue"><svg width="42" height="38" viewBox="0 0 42 38"><rect x="3" y="3" width="36" height="24" rx="2" fill="none" stroke="#fff" stroke-width="3"/><rect x="17" y="27" width="8" height="6" fill="#fff"/><rect x="11" y="32" width="20" height="3" fill="#fff"/></svg></div><span>vR Advise Products</span></div>
      <div class="offer-item"><div class="icon-circle dark"></div><span>Vendor Products</span></div>
    </div>
    <p>vR Advise developed products, complimentary solutions to our vendor products. From Pocketphone applications to cross-platform integrations for our Coreline and Vantaware product range.</p>
    <a class="btn btn-blue" href="#">Learn More</a>
    <a class="btn btn-green" href="#">Product List</a>
  </div>

  <div class="offer" style="left:795px">
    <h2>Support</h2>
    <div class="offer-icons">
      <div class="offer-item"><div class="icon-circle blue"><svg width="42" height="38" viewBox="0 0 42 38"><rect x="3" y="3" width="36" height="24" rx="2" fill="none" stroke="#fff" stroke-width="3"/><rect x="17" y="27" width="8" height="6" fill="#fff"/><rect x="11" y="32" width="20" height="3" fill="#fff"/></svg></div><span>Extended Support</span></div>
      <div class="offer-item"><div class="icon-circle orange"></div><span>Operational Support</span></div>
      <div class="offer-item"><div class="icon-circle dark"></div><span>Training</span></div>
    </div>
    <p>Offering training on the Coreline Sense and Watchpoint product range (as certified Coreline Training partners) as well as vR Advise developed product training. Customer training services also offered on request!</p>
    <a class="btn btn-blue" href="#">Learn More</a>
    <a class="btn btn-green" href="#">Training Courses</a>
  </div>
</section>

<section class="testimonials">
  <h2>Testimonials</h2>
  <div class="portrait" role="img" aria-label="Portrait photo of a smiling customer in a red shirt"></div>
  <blockquote class="quote">
    &ldquo; This is Pixelforge's version of Lorem Ipsum. Proin gravida nibh vel velit auctor aliquet. Aenean sollicitudin, lorem quis bibendum auctor, nisi elit consequat ipsum, nec sagittis sem nibh id elit. Duis sed odio sit amet nibh vulputate cursus a sit amet mauris. Morbi accumsan ipsum velit. &rdquo;
    <cite>Minerva, Northwind Company</cite>
  </blockquote>
  <div class="arrows">
    <svg width="22" height="16" viewBox="0 0 22 16"><path d="M9 2 3 8l6 6M3 8h17" fill="none" stroke="#b9d6f2" stroke-width="2"/></svg>
    <svg width="22" height="16" viewBox="0 0 22 16"><path d="M13 2l6 6-6 6M19 8H2" fill="none" stroke="#fff" stroke-width="2"/></svg>
  </div>
</section>

<section class="clients">
  <h2>Our Clients</h2>
  <div class="client-row">
    <div class="client">Halden Trading</div>
    <div class="client">Voltgrid</div>
    <div class="client">AREX</div>
    <div class="client">Penfold Financial</div>
    <div class="client">Loxley</div>
    <div class="client">Prism Data</div>
    <div class="client">Genvia</div>
  </div>
  <div class="arrows">
    <svg width="22" height="16" viewBox="0 0 22 16"><path d="M9 2 3 8l6 6M3 8h17" fill="none" stroke="#999" stroke-width="2"/></svg>
    <svg width="22" height="16" viewBox="0 0 22 16"><path d="M13 2l6 6-6 6M19 8H2" fill="none" stroke="#333" stroke-width="2"/></svg>
  </div>
</section>

<footer class="site-footer">
  <h2>Find Us</h2>
  <div class="social">
    <a href="#"><span class="dot"></span>Pagebook</a>
    <a href="#"><span class="dot"></span>Chirpr</a>
    <a href="#"><span class="dot"></span>Snapreel</a>
    <a href="#"><span class="dot"></span>Careernet</a>
    <a href="#"><span class="dot"></span>Orbitly</a>
  </div>
  <p class="copyright">Copyright vR Advise - 2013. All rights reserved.</p>
</footer>

</body>
</html>
```